Portugal:the best eco sun-dried tomato in the world needs a packaging design

We produce the best sun-dried tomatoes in the world...we know that, even that competition doesn´t exist...yet!
We are a "solar farm" in Portugal, reducing carbon footprint producing beautiful and healthy local food, with mules...the traditional way in a new way. Our tomatoes are hand-picked and sun dried, in a very "slow food" way.
The costumers for our product -we are a small farm - can only be good foodstores and airports, we'd love to export the best of Portugal elsewhere. In a glass jar of c. 250 ml, with a nice top and a nice logo+description...one that stands out of the others and conveys our eco, local, solar message.
Oh, and I forgot...our sun-dried tomatoes are packed with our beautiful olive oil..and yes, that olive oil has already won the best olive oil in the world! For sure!
I'll send photos for the interested, you'll love it; and the best olive oil and sun-dried tomatoes in the world for the winner!

Target Market(s)

nice foodstores
foodies
airport stores

Industry/Entity Type

Food Store

Font styles to use
Decorative
Script

Requirements
Must have
• Portugal
• Sun dried tomatoes
• Best olive oil in the world
• Traditional methods
• Sustainable farming
Nice to have
• a photo of our mules working...sent to interested designers

```html
<!DOCTYPE html>
<html lang="en">
<head>
<meta charset="utf-8">
<title>Solmira – Sun Dried Tomatoes Jar Labels</title>
<link href="https://fonts.googleapis.com/css2?family=Arimo:wght@400;700&display=swap" rel="stylesheet">
<style>
  :root {
    --backdrop: #ebe7ee;
    --label-red: #be1e2d;
    --deep-red: #a5121f;
    --paper: #ffffff;
    --tomato-light: #e9825a;
    --tomato-mid: #d4502f;
    --tomato-dark: #a8301c;
    --photo-light: #b5b5b5;
    --photo-dark: #2e2e2e;
    --blush: #f7c6c6;
  }
  html, body {
    margin: 0;
    padding: 0;
    overflow: hidden;
    background: var(--backdrop);
  }
  .canvas {
    position: relative;
    width: 1200px;
    height: 1000px;
    background: var(--backdrop);
  }
  .artwork { position: absolute; inset: 0; }
  .brand-name {
    font-family: "Arimo", Arial, sans-serif;
    font-weight: 700;
    fill: var(--paper);
  }
  .lid-tagline {
    font-family: "Arimo", Arial, sans-serif;
    font-size: 22px;
    fill: var(--paper);
    letter-spacing: 0.5px;
  }
  .panel-title {
    font-family: "Arimo", Arial, sans-serif;
    font-size: 14px;
    letter-spacing: 1.2px;
    fill: var(--paper);
  }
  .panel-claim {
    font-family: "Arimo", Arial, sans-serif;
    font-size: 10px;
    fill: var(--blush);
  }
  .panel-method {
    font-family: "Arimo", Arial, sans-serif;
    font-size: 12px;
    fill: var(--blush);
  }
  .lid-scallop { fill: var(--label-red); stroke: var(--label-red); stroke-width: 14; stroke-dasharray: 0 22; stroke-linecap: round; }
</style>
</head>
<body>
<div class="canvas">
<svg class="artwork" width="1200" height="1000" viewBox="0 0 1200 1000" xmlns="http://www.w3.org/2000/svg">
  <defs>
    <radialGradient id="tomatoTone" cx="50%" cy="45%" r="60%">
      <stop offset="0%" stop-color="var(--tomato-light)"/>
      <stop offset="60%" stop-color="var(--tomato-mid)"/>
      <stop offset="100%" stop-color="var(--tomato-dark)"/>
    </radialGradient>
    <linearGradient id="farmTone" x1="0" y1="0" x2="0" y2="1">
      <stop offset="0%" stop-color="var(--photo-light)"/>
      <stop offset="55%" stop-color="#6e6e6e"/>
      <stop offset="100%" stop-color="var(--photo-dark)"/>
    </linearGradient>
    <path id="ornateFrame" d="M70 18 Q280 -12 490 18 Q500 40 525 45 Q570 130 525 215 Q500 220 490 242 Q280 272 70 242 Q60 220 35 215 Q-10 130 35 45 Q60 40 70 18 Z"/>
    <path id="lidArc" d="M480 185 A100 100 0 0 0 680 185"/>
  </defs>

  <!-- Lid label -->
  <g class="lid-label">
    <circle class="lid-scallop" cx="580" cy="185" r="142"/>
    <circle cx="580" cy="185" r="142" fill="var(--label-red)"/>
    <circle cx="580" cy="185" r="130" fill="none" stroke="var(--paper)" stroke-width="5"/>
    <circle cx="580" cy="185" r="122" fill="url(#tomatoTone)" role="img" aria-label="Close-up of sun dried tomato slices"/>
    <circle cx="580" cy="185" r="122" fill="none" stroke="var(--deep-red)" stroke-width="2"/>
    <text class="brand-name" x="580" y="182" font-size="36" text-anchor="middle">Solmira</text>
    <text class="lid-tagline"><textPath href="#lidArc" startOffset="50%" text-anchor="middle">Sun dried tomatoes</textPath></text>
  </g>

  <!-- Front label, photo version -->
  <g class="front-label-photo">
    <g transform="translate(308 368) scale(1.0036 1.0154)">
      <use href="#ornateFrame" fill="var(--paper)" stroke="var(--label-red)" stroke-width="2"/>
      <g transform="translate(9 9) scale(0.9679 0.9308)">
        <use href="#ornateFrame" fill="url(#tomatoTone)" stroke="var(--label-red)" stroke-width="2" role="img" aria-label="Heap of sun dried tomatoes"/>
      </g>
    </g>
    <ellipse cx="576" cy="505" rx="66" ry="110" fill="url(#farmTone)" stroke="var(--paper)" stroke-width="4" role="img" aria-label="Black and white photo of farmers working with mules"/>
    <ellipse cx="576" cy="505" rx="68" ry="112" fill="none" stroke="var(--label-red)" stroke-width="1.5"/>
    <ellipse cx="590" cy="380" rx="47" ry="22" fill="var(--label-red)" stroke="var(--paper)" stroke-width="3"/>
    <text class="brand-name" x="590" y="385" font-size="14" text-anchor="middle">Solmira</text>
    <text class="panel-title" x="576" y="469" text-anchor="middle">SUN DRIED</text>
    <text class="panel-title" x="576" y="486" text-anchor="middle">TOMATOES</text>
    <text class="panel-claim" x="576" y="501" text-anchor="middle">Best olive oil in the world</text>
    <text class="panel-method" x="576" y="542" text-anchor="middle">Traditional methods</text>
    <text class="panel-claim" x="576" y="564" text-anchor="middle">Sustainable farming</text>
    <text class="panel-claim" x="576" y="585" text-anchor="middle">Portugal</text>
  </g>

  <!-- Front label, solid red version -->
  <g class="front-label-solid">
    <g transform="translate(310 672) scale(1 1.0615)">
      <use href="#ornateFrame" fill="var(--paper)" stroke="var(--label-red)" stroke-width="2"/>
      <g transform="translate(7 7) scale(0.975 0.946)">
        <use href="#ornateFrame" fill="var(--label-red)" stroke="var(--deep-red)" stroke-width="1.5"/>
      </g>
    </g>
    <ellipse cx="576" cy="828" rx="66" ry="112" fill="url(#farmTone)" stroke="var(--paper)" stroke-width="4" role="img" aria-label="Black and white photo of farmers working with mules"/>
    <ellipse cx="576" cy="828" rx="68" ry="114" fill="none" stroke="var(--deep-red)" stroke-width="1.5"/>
    <ellipse cx="590" cy="703" rx="47" ry="22" fill="var(--label-red)" stroke="var(--paper)" stroke-width="3"/>
    <text class="brand-name" x="590" y="708" font-size="14" text-anchor="middle">Solmira</text>
    <text class="panel-title" x="576" y="792" text-anchor="middle">SUN DRIED</text>
    <text class="panel-title" x="576" y="809" text-anchor="middle">TOMATOES</text>
    <text class="panel-claim" x="576" y="824" text-anchor="middle">Best olive oil in the world</text>
    <text class="panel-method" x="576" y="865" text-anchor="middle">Traditional methods</text>
    <text class="panel-claim" x="576" y="887" text-anchor="middle">Sustainable farming</text>
    <text class="panel-claim" x="576" y="908" text-anchor="middle">Portugal</text>
  </g>
</svg>
</div>
</body>
</html>
```